Financial Services business needs banner showcasing past stock picks

We are looking for a banner for our Vancouver B.C. based company named 'BrightLedger Financial'. Our website is www.ledgerpicks-demo.com and we provide several stock picking services to clients which we let them know which stocks to buy. We have an impressive track record of picking some of the best stocks on the Canadian and American stock markets and we would like to showcase some of these stocks to prospective clients at conferences.

```html
<!DOCTYPE html>
<html lang="en">
<head>
<meta charset="utf-8">
<title>BrightLedger Financial – Roll-up Banner</title>
<link href="https://fonts.googleapis.com/css2?family=Cinzel:wght@400&family=Mulish:wght@300;400&display=swap" rel="stylesheet">
<style>
  :root{
    --navy:#2f4453;
    --navy-deep:#2a3c4a;
    --teal:#20ab97;
    --teal-shade:#1c9483;
    --teal-band:#17907f;
    --paper:#efefef;
    --ink:#2f3e4b;
    --stage:#d6d6d6;
    --white:#ffffff;
  }
  html,body{margin:0;padding:0;width:923px;height:1200px;overflow:hidden;background:var(--stage);}
  .canvas{position:relative;width:923px;height:1200px;display:flex;align-items:center;justify-content:center;}
  .banner{width:515px;height:1160px;display:block;box-shadow:0 4px 18px rgba(0,0,0,.18);}
  .sans{font-family:"Mulish",sans-serif;}
  .serif{font-family:"Cinzel",serif;}
  .headline{fill:var(--white);font-weight:300;}
  .brand-name{fill:var(--teal);}
  .brand-word{fill:var(--ink);font-weight:400;}
  .tagline{fill:var(--ink);font-weight:400;letter-spacing:5px;}
  .web{fill:var(--white);font-weight:400;}
  .panel-text{fill:#333;font-size:7px;}
  .grid line{stroke:#dde2e6;stroke-width:.6;}
</style>
</head>
<body>
<main class="canvas">
<svg class="banner" viewBox="0 0 680 1532" preserveAspectRatio="none" xmlns="http://www.w3.org/2000/svg" aria-label="BrightLedger Financial banner">
  <defs>
    <linearGradient id="paperFade" x1="0" y1="0" x2="0" y2="1">
      <stop offset="0" stop-color="#f6f6f6"/>
      <stop offset="1" stop-color="#e4e4e4"/>
    </linearGradient>
    <linearGradient id="photoTone" x1="0" y1="0" x2="0.3" y2="1">
      <stop offset="0" stop-color="#e6f0ee"/>
      <stop offset="0.35" stop-color="#f4ece6"/>
      <stop offset="0.7" stop-color="#dde9f5"/>
      <stop offset="1" stop-color="#9fc2e6"/>
    </linearGradient>
  </defs>

  <!-- backgrounds -->
  <rect class="upper-field" x="0" y="0" width="680" height="803" fill="var(--navy)"/>
  <rect class="lower-field" x="0" y="803" width="680" height="655" fill="url(#paperFade)"/>

  <!-- photo area -->
  <polygon class="photo-area" role="img" aria-label="Photo of hands reviewing printed financial charts with a pen"
    points="494,0 680,0 680,710 472,977 330,803 210,437" fill="url(#photoTone)"/>

  <!-- right navy wedge -->
  <polygon class="corner-wedge" points="680,710 472,977 680,1287" fill="var(--navy-deep)"/>

  <!-- teal angled shapes -->
  <polygon class="angle-upper" points="407,0 494,0 210,437 187,560 27,560" fill="var(--teal)"/>
  <polygon class="angle-lower" points="210,437 452,803 347,803 187,560" fill="var(--teal)"/>
  <polygon class="angle-shade" points="157,362 210,437 130,560" fill="var(--teal-shade)"/>

  <!-- brand name top left -->
  <g class="brand-top">
    <rect x="92" y="60" width="80" height="80" fill="var(--teal)"/>
    <text class="serif brand-name" x="132" y="218" font-size="22" text-anchor="middle">BRIGHTLEDGER</text>
  </g>

  <!-- headline -->
  <g class="headline sans">
    <text x="30" y="637" font-size="62">ALL</text>
    <text x="30" y="693" font-size="40">WE DO IS</text>
    <text x="30" y="773" font-size="62">STOCKS</text>
  </g>

  <!-- chart one -->
  <g class="chart chart-one">
    <rect x="50" y="833" width="240" height="195" fill="#fff" stroke="#c9d0d6" stroke-width=".8"/>
    <g class="grid">
      <line x1="50" y1="863" x2="290" y2="863"/><line x1="50" y1="893" x2="290" y2="893"/>
      <line x1="50" y1="923" x2="290" y2="923"/><line x1="50" y1="963" x2="290" y2="963"/>
      <line x1="100" y1="833" x2="100" y2="1028"/><line x1="150" y1="833" x2="150" y2="1028"/>
      <line x1="200" y1="833" x2="200" y2="1028"/><line x1="250" y1="833" x2="250" y2="1028"/>
    </g>
    <line x1="50" y1="870" x2="272" y2="870" stroke="#6e8fc6" stroke-width="1"/>
    <polyline points="55,890 65,885 75,915 85,895 95,890 105,878 115,870 125,900 135,915 145,905 155,885 165,865 175,860 185,880 195,895 205,885 215,875 225,900 235,890 245,880 255,870 265,868 272,870" fill="none" stroke="#3d55a8" stroke-width="1.4"/>
    <polyline points="55,900 70,920 85,925 100,905 120,890 140,910 160,900 180,880 200,900 220,905 245,890 272,880" fill="none" stroke="#c0392b" stroke-width="1"/>
    <polyline points="55,935 75,930 95,915 120,905 145,920 170,900 195,905 220,915 250,895 272,885" fill="none" stroke="#7a9a3a" stroke-width=".8"/>
    <line x1="50" y1="968" x2="290" y2="968" stroke="#c9d0d6" stroke-width=".8"/>
    <path d="M56 990v-6M62 990v-9M68 990v-5M74 990v-8M80 990v-4M86 990v-10M92 990v-6M98 990v-7M104 990v-11M110 990v-5M116 990v-8M122 990v-6M128 990v-9M134 990v-4M140 990v-7M146 990v-10M152 990v-5M158 990v-8M164 990v-6M170 990v-9M176 990v-5M182 990v-7M188 990v-11M194 990v-6M200 990v-8M206 990v-5M212 990v-9M218 990v-6M224 990v-7M230 990v-10M236 990v-5M242 990v-8M248 990v-6M254 990v-9M260 990v-5M266 990v-7M272 990v-4" stroke="#2e9a4a" stroke-width="2.2"/>
    <polyline points="55,1010 70,1000 85,1018 100,1004 115,1015 130,1000 145,1016 160,1002 175,1017 190,1003 205,1015 220,1000 235,1016 250,1004 265,1014 280,1005" fill="none" stroke="#c0392b" stroke-width=".8" stroke-dasharray="2 1.5"/>
  </g>

  <!-- trade panel -->
  <g class="trade-panel sans">
    <rect x="53" y="1062" width="129" height="230" fill="#fff" stroke="#c9d0d6" stroke-width=".8"/>
    <text class="panel-text" x="104" y="1075" text-anchor="middle">Forex ▾</text>
    <line x1="53" y1="1081" x2="182" y2="1081" stroke="#dde2e6"/>
    <text class="panel-text" x="117" y="1093" text-anchor="middle" font-size="6">Instant Execution</text>
    <line x1="53" y1="1098" x2="182" y2="1098" stroke="#dde2e6"/>
    <text class="panel-text" x="62" y="1111" fill="#4a78c0" font-size="6">-0.01  -0.1</text>
    <text class="panel-text" x="110" y="1111" font-size="6">0.27</text>
    <text class="panel-text" x="140" y="1111" fill="#4a78c0" font-size="6">+0.01  +0.1</text>
    <text class="panel-text" x="63" y="1128" font-size="6">Stop Loss</text>
    <text class="panel-text" x="63" y="1145" font-size="6">Take Profit</text>
    <text class="panel-text" x="63" y="1162" font-size="6">Deviation</text>
    <rect x="53" y="1170" width="129" height="18" fill="#e3e3e3"/>
    <text class="panel-text" x="72" y="1183" font-size="8">1.2765</text>
    <text class="panel-text" x="137" y="1183" font-size="8">1.2765</text>
    <rect x="53" y="1188" width="65" height="16" fill="var(--teal)"/>
    <rect x="118" y="1188" width="64" height="16" fill="var(--navy)"/>
    <text x="85" y="1199" font-size="7" fill="#fff" text-anchor="middle">Sell</text>
    <text x="150" y="1199" font-size="7" fill="#fff" text-anchor="middle">Buy</text>
    <polyline points="60,1215 65,1222 70,1218 75,1240 82,1236 88,1252 95,1250 100,1262 110,1258 120,1262 135,1262 160,1263" fill="none" stroke="#8a3a3a" stroke-width="1"/>
    <rect x="163" y="1259" width="14" height="5" fill="#6e8fc6"/>
    <line x1="53" y1="1275" x2="460" y2="1275" stroke="#dde2e6"/>
  </g>

  <!-- chart two -->
  <g class="chart chart-two">
    <rect x="189" y="1062" width="271" height="213" fill="#fff" stroke="#c9d0d6" stroke-width=".8"/>
    <g class="grid">
      <line x1="189" y1="1092" x2="460" y2="1092"/><line x1="189" y1="1122" x2="460" y2="1122"/>
      <line x1="189" y1="1152" x2="460" y2="1152"/><line x1="189" y1="1182" x2="460" y2="1182"/>
      <line x1="243" y1="1062" x2="243" y2="1275"/><line x1="297" y1="1062" x2="297" y2="1275"/>
      <line x1="351" y1="1062" x2="351" y2="1275"/><line x1="405" y1="1062" x2="405" y2="1275"/>
    </g>
    <line x1="189" y1="1106" x2="445" y2="1106" stroke="#6e8fc6" stroke-width="1"/>
    <polyline points="195,1130 205,1125 215,1165 225,1140 235,1130 245,1115 255,1105 265,1140 275,1160 285,1150 295,1140 305,1135 315,1130 325,1120 335,1095 345,1090 355,1110 365,1120 375,1115 385,1125 395,1140 405,1125 415,1115 425,1110 435,1100 445,1106" fill="none" stroke="#3d55a8" stroke-width="1.4"/>
    <polyline points="195,1175 215,1180 235,1150 255,1140 275,1170 295,1160 315,1150 335,1120 355,1125 375,1140 395,1150 415,1130 445,1120" fill="none" stroke="#7a9a3a" stroke-width=".8"/>
    <polyline points="195,1150 215,1160 235,1140 255,1125 275,1150 300,1145 320,1135 340,1110 360,1115 380,1130 400,1140 420,1125 445,1115" fill="none" stroke="#c0392b" stroke-width="1"/>
    <line x1="189" y1="1212" x2="460" y2="1212" stroke="#c9d0d6" stroke-width=".8"/>
    <path d="M196 1240v-6M203 1240v-9M210 1240v-5M217 1240v-8M224 1240v-4M231 1240v-10M238 1240v-6M245 1240v-7M252 1240v-11M259 1240v-5M266 1240v-8M273 1240v-6M280 1240v-9M287 1240v-4M294 1240v-7M301 1240v-10M308 1240v-5M315 1240v-8M322 1240v-6M329 1240v-9M336 1240v-5M343 1240v-7M350 1240v-11M357 1240v-6M364 1240v-8M371 1240v-5M378 1240v-9M385 1240v-6M392 1240v-7M399 1240v-10M406 1240v-5M413 1240v-8M420 1240v-6M427 1240v-9M434 1240v-5M441 1240v-7" stroke="#2e9a4a" stroke-width="2.4"/>
    <polyline points="195,1262 210,1250 225,1266 240,1252 255,1265 270,1250 285,1266 300,1252 315,1265 330,1250 345,1266 360,1252 375,1265 390,1250 405,1266 420,1252 435,1264 450,1254" fill="none" stroke="#c0392b" stroke-width=".8" stroke-dasharray="2 1.5"/>
  </g>

  <!-- company name block -->
  <g class="company">
    <text class="serif brand-name" x="50" y="1382" font-size="38" textLength="292" lengthAdjust="spacingAndGlyphs">BRIGHTLEDGER</text>
    <line x1="358" y1="1326" x2="358" y2="1390" stroke="var(--ink)" stroke-width="2"/>
    <text class="sans brand-word" x="372" y="1380" font-size="46" textLength="258" lengthAdjust="spacingAndGlyphs">FINANCIAL</text>
    <text class="sans tagline" x="48" y="1432" font-size="23" textLength="584" lengthAdjust="spacing">INDEPENDENT EQUITY ADVISORS</text>
  </g>

  <!-- web band -->
  <rect class="web-band" x="0" y="1458" width="680" height="74" fill="var(--teal-band)"/>
  <text class="sans web" x="340" y="1507" font-size="34" text-anchor="middle">www.ledgerpicks-demo.com</text>
</svg>
</main>
</body>
</html>
```